Black Car Limousine transportation business in Naples Florida

Brightway stand for my reliability and DPR stands for Devotion, P and R are the first initials of my children's names. It should show professionalism and a dedication to customer service. We keep our clients identities private. Show our professionalism. We are Black car Black tie company. We service transportation on a reserve basis to and from residents, airports, casinos, hotels,

Target Market(s)

It is a Private car service. High end clients. Businesses, Celebrity and athletes. Service to airports, hotels, special events.

Industry/Entity Type

Business

Contact Information for Business Card

A pearl metallic or Luster card. Standard business card size. Would like the name, Company email, show we take credit cards and phone number. Currently I don't have a website but will like to add later.

Logo Text

BRIGHTWAY DPR TRANSPORTATION

Font styles to use
Serif

Colors
eaeaea
000000

Requirements
Must have
• Must have Company email, show we take credit cards and phone number. Currently I don't have a website but will like to add later.
Nice to have
• Would like to stay with a black and white theme. Open to some color trim.
Should not have
• Open to suggestions

```html
<!DOCTYPE html>
<html lang="en">
<head>
<meta charset="utf-8">
<title>Brightway DPR Transportation – Business Card</title>
<link rel="stylesheet" href="https://fonts.googleapis.com/css2?family=Open+Sans:ital,wght@0,400;0,600;0,700;1,700&display=swap">
<style>
  :root {
    --backdrop: #bdbdbd;
    --card-white: #ffffff;
    --card-black: #000000;
    --ink: #111111;
    --ink-soft: #333333;
    --silver: #9a9a9a;
    --silver-light: #c8c8c8;
    --band-grey: #9e9e9e;
    --vehicle-dark: #1a1a1a;
    --vehicle-mid: #5a5a5a;
  }
  * { margin: 0; padding: 0; box-sizing: border-box; }
  html, body {
    width: 1105px; height: 1200px; overflow: hidden;
    background: var(--backdrop);
    font-family: "Open Sans", Arial, sans-serif;
  }
  .card {
    position: absolute; left: 193px; width: 720px; height: 412px;
    overflow: hidden;
    box-shadow: 0 4px 10px rgba(0,0,0,0.35);
  }
  .card--front { top: 167px; background: var(--card-white); }
  .card--back { top: 623px; background: var(--card-black); }

  .vehicle {
    position: absolute; border-radius: 10px 14px 6px 6px;
    background: linear-gradient(180deg, var(--vehicle-mid) 0%, var(--vehicle-dark) 60%, var(--vehicle-mid) 100%);
  }
  .wordmark {
    position: absolute; font-weight: 700; line-height: 1; text-align: left;
    color: var(--silver);
  }
  .wordmark span { display: block; }
  .wordmark .wm-top { font-size: 0.5em; letter-spacing: 0.04em; }
  .wordmark .wm-main { font-size: 1em; letter-spacing: 0.02em; }
  .wordmark .wm-sub { font-size: 0.36em; letter-spacing: 0.12em; }

  .card--front .vehicle { left: 50px; top: 84px; width: 118px; height: 48px; }
  .card--front .wordmark { left: 178px; top: 60px; font-size: 46px; }

  .contact { position: absolute; right: 40px; text-align: right; color: var(--ink-soft); }
  .contact__name { top: 156px; font-size: 25px; font-weight: 700; color: var(--ink); letter-spacing: 0.01em; }
  .contact__title { top: 189px; font-size: 20px; }
  .contact__line { font-size: 18px; display: flex; align-items: center; gap: 10px; }
  .contact__phone { top: 286px; }
  .contact__email { top: 313px; }
  .contact__line svg { width: 18px; height: 18px; fill: var(--ink); }

  .band-grey { position: absolute; left: 0; bottom: 0; width: 380px; height: 16px; background: var(--band-grey); }
  .band-black { position: absolute; right: 0; bottom: 0; width: 720px; height: 49px; }
  .web {
    position: absolute; right: 36px; bottom: 12px;
    color: var(--card-white); font-size: 19px; letter-spacing: 0.2em;
  }

  .card--back .vehicle { left: 138px; top: 178px; width: 177px; height: 70px; background: linear-gradient(180deg, #6a6a6a 0%, #2a2a2a 60%, #7a7a7a 100%); }
  .card--back .wordmark { left: 329px; top: 140px; font-size: 66px; color: var(--silver-light); }

  .payment {
    position: absolute; left: 0; right: 0; top: 336px;
    display: flex; justify-content: center; align-items: center; gap: 10px;
    color: var(--card-white); font-size: 19px; font-weight: 700; font-style: italic;
  }
  .payment svg { width: 26px; height: 20px; }
</style>
</head>
<body>
  <section class="card card--front">
    <div class="vehicle" role="img" aria-label="Photo of a black luxury SUV"></div>
    <div class="wordmark">
      <span class="wm-top">BRIGHTWAY</span>
      <span class="wm-main">DPR</span>
      <span class="wm-sub">TRANSPORTATION</span>
    </div>

    <p class="contact contact__name">DANIEL REEVES</p>
    <p class="contact contact__title">CEO/Founder</p>
    <p class="contact contact__line contact__phone">239 555 0187
      <svg viewBox="0 0 24 24" aria-hidden="true"><path d="M6.6 10.8a15.1 15.1 0 0 0 6.6 6.6l2.2-2.2c.3-.3.7-.4 1-.2 1.1.4 2.3.6 3.6.6.6 0 1 .4 1 1V20c0 .6-.4 1-1 1C10.6 21 3 13.4 3 4c0-.6.4-1 1-1h3.5c.6 0 1 .4 1 1 0 1.3.2 2.5.6 3.6.1.3 0 .7-.2 1z"/></svg>
    </p>
    <p class="contact contact__line contact__email">info@brightwaydpr.com
      <svg viewBox="0 0 24 24" aria-hidden="true"><path d="M2 5h20v14H2z M2 5l10 8 10-8" /></svg>
    </p>

    <div class="band-grey"></div>
    <svg class="band-black" viewBox="0 0 720 49" preserveAspectRatio="none" aria-hidden="true">
      <polygon points="355,49 373,38 390,38 400,31 400,20 430,0 720,0 720,49" fill="#ffffff"/>
      <polygon points="366,49 410,20 425,20 440,0 720,0 720,49" fill="#000000"/>
    </svg>
    <p class="web">www.brightwaydpr.com</p>
  </section>

  <section class="card card--back">
    <div class="vehicle" role="img" aria-label="Photo of a black luxury SUV"></div>
    <div class="wordmark">
      <span class="wm-top">BRIGHTWAY</span>
      <span class="wm-main">DPR</span>
      <span class="wm-sub">TRANSPORTATION</span>
    </div>
    <p class="payment">
      <svg viewBox="0 0 26 20" aria-hidden="true"><rect x="1" y="2" width="24" height="16" rx="3" fill="#ffffff"/><rect x="1" y="6" width="24" height="3" fill="#000000"/><rect x="4" y="12" width="8" height="2" fill="#000000"/></svg>
      We accept credit cards
    </p>
  </section>
</body>
</html>
```